Architectural, Engineering and Design Build

Tavonex4.com
Veteran Disabled Certified company is doing business in Architecture, Engineer and Design build - look simialr websites and come up with design follow following website
https://dorsey-kalbin.example/
https://www.velmonteam.example/
https://www.pirnoqa.example/contract-vehicles/service-disabled-veteran-owned-small-business-sdvosb/
https://www.corbelhubnet.example/about/sdvosb/

Target Market(s)

US - Defense and Federal Government

Industry/Entity Type

Colors
0054AA
0677BA
7BADD7
CADEEF
E8F1F8

Requirements
Must have
• Army, American patriotism , Buildings, construction, architecture, engineering
Nice to have
• I need to attract federal government agencies and Defense

```html
<!DOCTYPE html>
<html lang="en">
<head>
<meta charset="utf-8">
<title>Tavonex4 — Architecture, Engineering &amp; Design Build</title>
<link href="https://fonts.googleapis.com/css2?family=Rajdhani:wght@600;700&family=Roboto:wght@400;500;700&display=swap" rel="stylesheet">
<style>
:root{
  --red:#e3121c;
  --red-dark:#b80d15;
  --navy:#151d5e;
  --navy-deep:#0e1547;
  --ink:#222;
  --muted:#6b6b6b;
  --paper:#ffffff;
  --blush:#fbf1f1;
  --night:#120d0e;
}
*{margin:0;padding:0;box-sizing:border-box}
html,body{width:1200px;height:4699px;overflow:hidden}
body{position:relative;background:var(--paper);font-family:Roboto,Arial,sans-serif;color:var(--ink)}
.abs{position:absolute}
.display{font-family:Rajdhani,"Arial Narrow",sans-serif;font-weight:700;letter-spacing:1px;text-transform:uppercase}
.btn{position:absolute;display:flex;align-items:center;justify-content:center;border-radius:30px;color:#fff;font-weight:700;font-size:17px}
.btn-red{background:var(--red)}
.btn-navy{background:var(--navy)}

/* header */
.site-header{position:absolute;left:0;top:0;width:1200px;height:170px;background:#fff;z-index:5}
.brand-badge{position:absolute;left:104px;top:20px;width:230px;height:230px;border-radius:50%;background:#fff;z-index:6;display:flex;align-items:center;justify-content:center}
.brand-name{font-family:Rajdhani,sans-serif;font-weight:700;font-size:40px;color:var(--navy);letter-spacing:1px}
.contact-item{position:absolute;top:26px;display:flex;align-items:center;gap:18px}
.contact-icon{width:46px;height:46px;border-radius:50%;background:var(--navy);display:flex;align-items:center;justify-content:center}
.contact-label{font-size:12px;color:var(--ink)}
.contact-value{font-size:18px;font-weight:500;color:var(--ink);margin-top:4px}
.main-nav{position:absolute;left:374px;top:106px;width:826px;height:64px;background:var(--red);border-radius:14px 0 0 0;display:flex;align-items:center;padding-left:40px}
.main-nav a{color:#fff;text-decoration:none;font-size:14px;font-weight:500;margin-right:58px}
.main-nav .join{background:var(--navy);padding:11px 38px;border-radius:20px;margin-left:-8px}

/* hero */
.hero{position:absolute;left:0;top:170px;width:1200px;height:700px;background:radial-gradient(ellipse at 50% 20%,#4b4f62 0%,#2a2c38 45%,#141318 100%)}
.hero-title{position:absolute;top:400px;width:1200px;text-align:center;font-size:60px;color:#fff}
.hero-title span{color:var(--red)}
.hero-copy{position:absolute;top:490px;width:1200px;text-align:center;font-size:18px;line-height:38px;color:#fff}

/* about */
.about{position:absolute;left:0;top:857px;width:1200px;height:760px;background:linear-gradient(160deg,#fff 0%,var(--blush) 35%,#f8e4e4 55%,#fff 80%)}
.section-title{font-size:44px;color:#111}
.body-copy{font-size:13.5px;line-height:31.5px;color:var(--muted)}

/* offer */
.offer-card{position:absolute;top:1851px;width:314px;height:433px;border-radius:28px;overflow:hidden;color:#fff}
.offer-photo{height:221px;width:100%}
.offer-body{padding:68px 33px 0}
.offer-card h3{font-size:20px;margin-bottom:14px}
.offer-card p{font-size:11.5px;line-height:25px}
.offer-card .more{font-size:11.5px;text-decoration:underline;margin-top:10px;display:block}
.offer-icon{position:absolute;left:33px;top:192px;width:64px;height:64px;border-radius:50%;background:var(--red);border:3px solid #fff;display:flex;align-items:center;justify-content:center}

/* blogs */
.blog-card{position:absolute;top:3285px;width:314px}
.blog-photo{height:257px;width:100%}
.blog-date{position:absolute;left:24px;top:246px;background:var(--red);color:#fff;font-size:12px;font-weight:700;padding:7px 14px;border-radius:8px}
.blog-card h4{margin:38px 24px 0;font-size:13.5px;line-height:28px;color:#111}
.blog-card p{margin:12px 24px 0;font-size:10.5px;line-height:22px;color:var(--muted)}
.round-arrow{position:absolute;width:34px;height:34px;border-radius:50%;background:#fff;box-shadow:0 2px 8px rgba(0,0,0,.2);display:flex;align-items:center;justify-content:center;color:var(--navy);font-size:14px;font-weight:700}

/* contact */
.field{position:absolute;background:var(--navy);border-radius:8px;color:#fff;font-size:12px;padding:13px 16px}

/* footer */
.site-footer{position:absolute;left:0;top:4104px;width:1200px;height:595px;background:linear-gradient(160deg,#3a0a0d 0%,var(--night) 40%,#1a0c0d 100%)}
.footer-nav{position:absolute;top:4552px;width:1200px;display:flex;justify-content:center}
.footer-nav a{color:#fff;text-decoration:none;font-size:14px;font-weight:500;margin:0 40px}
.social{position:absolute;top:4584px;left:507px;display:flex;gap:14px}
.social span{width:38px;height:38px;border-radius:50%;background:var(--red);display:block}
.copyright{position:absolute;top:4652px;width:1200px;text-align:center;font-size:11px;color:#ddd}
</style>
</head>
<body>

<!-- Header -->
<header class="site-header">
  <div class="contact-item" style="left:645px">
    <div class="contact-icon"><svg width="16" height="16" viewBox="0 0 24 24"><path fill="#fff" d="M6.6 10.8a15 15 0 0 0 6.6 6.6l2.2-2.2c.3-.3.7-.4 1-.2 1.1.4 2.3.6 3.6.6.6 0 1 .4 1 1V20c0 .6-.4 1-1 1A17 17 0 0 1 3 4c0-.6.4-1 1-1h3.5c.6 0 1 .4 1 1 0 1.3.2 2.5.6 3.6.1.3 0 .7-.2 1z"/></svg></div>
    <div><div class="contact-label">Call Us:</div><div class="contact-value">+1 888 888 8888</div></div>
  </div>
  <div class="contact-item" style="left:884px">
    <div class="contact-icon"><svg width="18" height="14" viewBox="0 0 24 18"><path fill="#fff" d="M2 0h20c1.1 0 2 .9 2 2v14c0 1.1-.9 2-2 2H2c-1.1 0-2-.9-2-2V2C0 .9.9 0 2 0zm10 8L2.5 2h19z"/></svg></div>
    <div><div class="contact-label">Email Us:</div><div class="contact-value">info@tavonex4.example</div></div>
  </div>
  <nav class="main-nav">
    <a>Home</a><a>About Us</a><a>Services</a><a>Reviews</a><a>Contact Us</a><a class="join">Join With Us</a>
  </nav>
</header>
<div class="brand-badge"><span class="brand-name">TAVONEX4</span></div>

<!-- Hero -->
<section class="hero" role="img" aria-label="Dusk sky with a monument silhouette and a faint flag overlay"></section>
<h1 class="hero-title display">Welcome to <span>Tavonex4</span></h1>
<p class="hero-copy">Lorem ipsum dolor sit amet, consectetur adipiscing elit, sed do eiusmod tempor incididunt ut labore<br>et dolore magna aliqua. Quis ipsum suspendisse ultrices gravida.</p>
<div class="btn btn-red" style="left:419px;top:601px;width:146px;height:42px">Get Started</div>
<div class="btn btn-navy" style="left:592px;top:601px;width:188px;height:42px">+1 888 888 8888</div>

<!-- About -->
<section class="about" role="img" aria-label="Soft waving flag backdrop in pale red and white"></section>
<svg class="abs" style="left:0;top:740px" width="1200" height="140" viewBox="0 0 1200 140">
  <path d="M0 20 Q600 200 1200 20 V140 H0Z" fill="#fff"/>
  <path d="M0 20 Q600 200 1200 20" fill="none" stroke="var(--red)" stroke-width="5"/>
  <path d="M0 36 Q600 216 1200 36" fill="none" stroke="var(--navy)" stroke-width="3"/>
</svg>
<div class="abs" style="left:573px;top:835px;width:56px;height:56px;border-radius:50%;background:#fff;border:2px solid var(--navy);display:flex;align-items:center;justify-content:center">
  <svg width="14" height="24" viewBox="0 0 14 24"><path d="M7 0 13 8H1zM7 24 1 16h12z" fill="var(--navy)"/><circle cx="7" cy="12" r="2" fill="var(--red)"/></svg>
</div>

<div class="abs" style="left:122px;top:1018px;width:456px;height:456px;border-radius:50%;border:3px solid var(--red);background:#fff"></div>
<div class="abs" style="left:138px;top:1034px;width:424px;height:424px;border-radius:50%;background:var(--navy)"></div>
<div class="abs" style="left:164px;top:1060px;width:372px;height:372px;border-radius:50%;background:linear-gradient(180deg,#cfd4dd 0%,#e8c79a 45%,#8a7a4e 80%,#4d4a35 100%)" role="img" aria-label="Soldier carrying a child holding a flag in a field at sunset"></div>

<h2 class="abs display section-title" style="left:638px;top:1040px">About Us</h2>
<p class="abs body-copy" style="left:638px;top:1104px;width:440px">Lorem ipsum dolor sit amet, consectetur adipiscing elit, sed do eiusmod tempor incididunt ut labore et dolore magna aliqua. Quis ipsum suspendisse ultrices gravida. Risus commodo viverra maecenas accumsan lacus vel facilisis. Lorem ipsum dolor sit amet, consectetur adipiscing elit, sed do eiusmod tempor incididunt ut labore et dolore magna aliqua. Quis ipsum suspendisse ultrices gravida.</p>
<p class="abs body-copy" style="left:638px;top:1325px;width:440px">Consectetur adipiscing elit, sed do eiusmod tempor incididunt ut labore et dolore magna aliqua.</p>
<div class="btn btn-red" style="left:638px;top:1411px;width:120px;height:38px;font-size:13px">Read More</div>

<!-- What we offer -->
<svg class="abs" style="left:0;top:1605px" width="1200" height="120" viewBox="0 0 1200 120">
  <path d="M0 110 Q600 -60 1200 110" fill="none" stroke="var(--navy)" stroke-width="5"/>
</svg>
<div class="abs" style="left:0;top:1780px;width:1200px;height:600px;background:linear-gradient(180deg,#fff 0%,#f7e8ea 40%,#f2dfe2 75%,#fff 100%)" role="img" aria-label="Faint flag with stars in the background"></div>
<h2 class="abs display section-title" style="left:0;width:1200px;text-align:center;top:1690px">What We Offer</h2>
<p class="abs body-copy" style="left:0;width:1200px;text-align:center;top:1758px;font-size:13px;line-height:29px">Lorem ipsum dolor sit amet, consectetur adipiscing elit, sed do eiusmod tempor incididunt ut labore et dolore magna aliqua.<br>Quis ipsum suspendisse ultrices gravida. Risus commodo viverra maecenas accumsan lacus vel facilisis.</p>

<article class="offer-card" style="left:113px;background:var(--red)">
  <div class="offer-photo" style="background:linear-gradient(135deg,#f2f0ec,#c9c2b6)" role="img" aria-label="Hands drafting a floor plan"></div>
  <div class="offer-icon"><svg width="28" height="28" viewBox="0 0 24 24" fill="none" stroke="#fff" stroke-width="1.6"><rect x="3" y="3" width="18" height="18"/><path d="M7 17 17 7M13 7h4v4"/></svg></div>
  <div class="offer-body"><h3 class="display">Architecture</h3><p>Lorem ipsum dolor sit amet, consectetur adipiscing elit, sed do eiusmod tempor incididunt ut labore et dolore magna aliqua.</p><span class="more">View More</span></div>
</article>
<article class="offer-card" style="left:443px;background:var(--navy)">
  <div class="offer-photo" style="background:linear-gradient(180deg,#6f98c8,#c7d5e4 60%,#9a9488)" role="img" aria-label="Engineers on a construction site with cranes"></div>
  <div class="offer-icon"><svg width="28" height="28" viewBox="0 0 24 24" fill="none" stroke="#fff" stroke-width="1.6"><circle cx="12" cy="12" r="4"/><path d="M12 2v4M12 18v4M2 12h4M18 12h4M5 5l3 3M16 16l3 3M5 19l3-3M16 8l3-3"/></svg></div>
  <div class="offer-body"><h3 class="display">Engineering</h3><p>Lorem ipsum dolor sit amet, consectetur adipiscing elit, sed do eiusmod tempor incididunt ut labore et dolore magna aliqua.</p><span class="more">View More</span></div>
</article>
<article class="offer-card" style="left:773px;background:var(--red)">
  <div class="offer-photo" style="background:linear-gradient(135deg,#eceae6,#b9b3a8)" role="img" aria-label="Sketch of a modern building turning into the finished house"></div>
  <div class="offer-icon"><svg width="28" height="28" viewBox="0 0 24 24" fill="none" stroke="#fff" stroke-width="1.6"><path d="M12 3 4 21M12 3l8 18M7 14h10"/><circle cx="12" cy="3" r="1.5"/></svg></div>
  <div class="offer-body"><h3 class="display">Design Build</h3><p>Lorem ipsum dolor sit amet, consectetur adipiscing elit, sed do eiusmod tempor incididunt ut labore et dolore magna aliqua.</p><span class="more">View More</span></div>
</article>

<!-- Testimonials -->
<div class="abs" style="left:0;top:2379px;width:1200px;height:620px;background:linear-gradient(160deg,#c9a57a 0%,#f0d9a8 35%,#9a8a80 60%,#4a4548 100%)" role="img" aria-label="Man raising a large flag against a sunset sky"></div>
<svg class="abs" style="left:0;top:2379px" width="1200" height="620" viewBox="0 0 1200 620">
  <path d="M0 0H520L650 620H0Z" fill="var(--navy)"/>
  <path d="M0 520 Q600 650 1200 520 V620 H0Z" fill="#fff"/>
  <path d="M0 505 Q600 635 1200 505" fill="none" stroke="var(--navy)" stroke-width="5"/>
  <path d="M0 520 Q600 650 1200 520" fill="none" stroke="var(--red)" stroke-width="4"/>
</svg>
<h2 class="abs display" style="left:113px;top:2470px;font-size:42px;color:#fff">Testimonials</h2>
<div class="abs" style="left:113px;top:2548px;font-family:Georgia,serif;font-size:80px;line-height:1;color:#fff;font-weight:700">”</div>
<p class="abs" style="left:113px;top:2620px;width:410px;font-size:13.5px;line-height:31.5px;color:#fff">I must explain to you how all this mistaken idea of denouncing pleasure and praising pain was born and I will give you a complete account of the system, and expound the actual teachings of the great explorer of the truth</p>
<p class="abs" style="left:113px;top:2777px;width:410px;font-size:13.5px;line-height:31.5px;color:#fff">No one rejects, dislikes, or avoids pleasure itself, because it is pleasure.</p>
<div class="abs" style="left:113px;top:2855px;font-size:13.5px;color:var(--red);text-transform:uppercase">Darin Kesslow</div>
<div class="round-arrow" style="left:484px;top:2904px">«</div>
<div class="round-arrow" style="left:531px;top:2904px">»</div>

<!-- Blogs -->
<h2 class="abs display section-title" style="left:0;width:1200px;text-align:center;top:3120px">Latest Blogs &amp; News</h2>
<p class="abs body-copy" style="left:0;width:1200px;text-align:center;top:3185px;font-size:13px;line-height:29px">Lorem ipsum dolor sit amet, consectetur adipiscing elit, sed do eiusmod tempor incididunt ut labore et dolore magna aliqua.<br>Quis ipsum suspendisse ultrices gravida. Risus commodo viverra maecenas accumsan lacus vel facilisis.</p>
<div class="round-arrow" style="left:36px;top:3474px">«</div>
<div class="round-arrow" style="left:1128px;top:3474px">»</div>

<article class="blog-card" style="left:113px">
  <div class="blog-photo" style="background:linear-gradient(135deg,#f3f1ec,#cfcac0)" role="img" aria-label="Architectural plans with sticky notes on a desk"></div>
  <span class="blog-date">13/06/2024</span>
  <h4>Lorem ipsum dolor sit amet, consectetur adipiscing elit, sed do eiusmod</h4>
  <p>Lorem ipsum dolor sit amet, consectetur adipiscing elit, sed do eiusmod tempor incididunt ut labore et dolore magna aliqua. Quis ipsum suspendisse ultrices gravida.</p>
</article>
<article class="blog-card" style="left:443px">
  <div class="blog-photo" style="background:linear-gradient(180deg,#2f5fa8,#1c2f55 55%,#b2703a)" role="img" aria-label="Glass office tower lit at dusk"></div>
  <span class="blog-date">13/06/2024</span>
  <h4>Lorem ipsum dolor sit amet, consectetur adipiscing elit, sed do eiusmod</h4>
  <p>Lorem ipsum dolor sit amet, consectetur adipiscing elit, sed do eiusmod tempor incididunt ut labore et dolore magna aliqua. Quis ipsum suspendisse ultrices gravida.</p>
</article>
<article class="blog-card" style="left:773px">
  <div class="blog-photo" style="background:linear-gradient(135deg,#3a3232,#8a5a4a 55%,#d9a57f)" role="img" aria-label="Soldier saluting in front of a flag"></div>
  <span class="blog-date">13/06/2024</span>
  <h4>Lorem ipsum dolor sit amet, consectetur adipiscing elit, sed do eiusmod</h4>
  <p>Lorem ipsum dolor sit amet, consectetur adipiscing elit, sed do eiusmod tempor incididunt ut labore et dolore magna aliqua. Quis ipsum suspendisse ultrices gravida.</p>
</article>

<!-- Footer background -->
<footer class="site-footer" role="img" aria-label="Dark backdrop with red flag stripes"></footer>
<svg class="abs" style="left:0;top:4104px" width="1200" height="120" viewBox="0 0 1200 120">
  <path d="M0 40 Q600 130 1200 40" fill="none" stroke="var(--red)" stroke-width="8"/>
</svg>

<!-- Contact -->
<section class="abs" style="left:113px;top:3825px;width:974px;height:498px;border-radius:36px;background:linear-gradient(135deg,var(--red) 0%,#f03a3f 50%,var(--red-dark) 100%)" aria-label="Contact"></section>
<div class="abs" style="left:144px;top:3867px;width:410px;height:416px;border-radius:26px;background:linear-gradient(180deg,#c9ccd3 0%,#8f8c86 50%,#3c3a36 100%)" role="img" aria-label="Soldier in uniform saluting at sunrise"></div>
<h2 class="abs display" style="left:606px;top:3880px;font-size:42px;color:#fff">Get In Touch</h2>
<p class="abs" style="left:606px;top:3940px;font-size:14px;color:#fff">We denounce with righteous indignation and dislike men</p>
<div class="field" style="left:606px;top:3984px;width:212px;height:40px">First Name</div>
<div class="field" style="left:839px;top:3984px;width:212px;height:40px">Last Name</div>
<div class="field" style="left:606px;top:4049px;width:212px;height:41px">Email Address</div>
<div class="field" style="left:839px;top:4049px;width:212px;height:41px">Contact Number</div>
<div class="field" style="left:606px;top:4115px;width:445px;height:107px">Message</div>
<div class="abs" style="left:606px;top:4244px;font-size:12px;font-weight:700;color:#fff;text-decoration:underline;letter-spacing:.5px">SEND MESSAGE</div>

<!-- Footer content -->
<div class="abs" style="left:505px;top:4382px;width:190px;height:140px;display:flex;align-items:center;justify-content:center">
  <span class="brand-name" style="color:#fff;font-size:38px">TAVONEX4</span>
</div>
<nav class="footer-nav"><a>Home</a><a>About Us</a><a>Services</a><a>Reviews</a><a>Contact Us</a></nav>
<div class="social" aria-label="Social links"><span></span><span></span><span></span><span></span></div>
<p class="copyright">(C) Copyright 2024 | All Rights Reserved</p>

</body>
</html>
```